Orvel Prime - Letter Head

My company is a residential and commercial cleaning company , which is located in Abu Dhabi, UAE.
I am looking for a creative letterhead reflects the professional and reflects professionalism and send the feeling of relax and comfort.
The color which will be used it has to be selected carefully in prospective of colors psychological effects, so every color to be used should be for a reason.
Also, reflecting my company colors in an attractive way.
Regarding the information which it should contains, it has to show the address, contacts , telephones an, email address and website.
Also, my company logo is attached
Residential

```html
<!DOCTYPE html>
<html lang="en">
<head>
<meta charset="utf-8">
<title>Orvel Prime – Letterhead</title>
<link rel="stylesheet" href="https://fonts.googleapis.com/css2?family=Poppins:wght@400;600&display=swap">
<style>
  :root {
    --paper: #ffffff;
    --brand-blue: #1a7cc4;
    --brand-green: #8cc63f;
    --wave-light: #3ea9df;
    --wave-mid: #2f9fd8;
    --wave-deep: #0a8fcf;
    --contact-accent: #cfe23b;
    --footer-text: #ffffff;
  }
  html, body {
    margin: 0;
    padding: 0;
    overflow: hidden;
    background: var(--paper);
  }
  .letterhead {
    position: relative;
    width: 849px;
    height: 1200px;
    background: var(--paper);
    overflow: hidden;
    font-family: "Poppins", sans-serif;
  }
  .brand {
    position: absolute;
    top: 92px;
    right: 56px;
    display: flex;
    align-items: center;
    gap: 16px;
  }
  .brand-name {
    font-size: 52px;
    font-weight: 600;
    line-height: 1;
    color: var(--brand-blue);
    letter-spacing: -0.5px;
  }
  .brand-dot {
    width: 44px;
    height: 44px;
    border-radius: 50%;
    background: var(--brand-green);
  }
  .footer-waves {
    position: absolute;
    left: 0;
    top: 0;
    width: 849px;
    height: 1200px;
  }
  .footer-contact {
    position: absolute;
    left: 51px;
    right: 40px;
    bottom: 0;
    top: 1088px;
    color: var(--footer-text);
  }
  .address {
    margin: 0;
    font-size: 16.5px;
    font-weight: 400;
    letter-spacing: 0.1px;
  }
  .contact-line {
    margin: 14px 0 0;
    font-size: 22px;
    font-weight: 600;
    color: var(--contact-accent);
    white-space: nowrap;
  }
  .contact-line .divider {
    color: var(--footer-text);
    font-weight: 400;
    margin: 0 12px;
  }
</style>
</head>
<body>
  <main class="letterhead">
    <header class="brand">
      <span class="brand-name">Orvel Prime</span>
      <span class="brand-dot"></span>
    </header>

    <svg class="footer-waves" viewBox="0 0 849 1200" aria-hidden="true">
      <path class="swoosh-upper" d="M0,1016 Q450,1072 849,776 L849,806 Q470,1078 0,1028 Z" fill="var(--wave-light)"/>
      <path class="wave-mid" d="M0,1018 Q520,1100 849,836 L849,1200 L0,1200 Z" fill="var(--wave-mid)"/>
      <path class="wave-deep" d="M0,1052 Q480,1095 849,888 L849,1200 L0,1200 Z" fill="var(--wave-deep)"/>
    </svg>

    <footer class="footer-contact">
      <p class="address">Address Line 1, Address Line 2, Address Line 3, Address Line 4, Address Line 5</p>
      <p class="contact-line">
        <span class="phone">Telephone No.</span><span class="divider">|</span><span class="email">info@orvelprime.com</span><span class="divider">|</span><span class="website">www.orvelprime.com</span>
      </p>
    </footer>
  </main>
</body>
</html>
```